Website design in Wordpress for Golf Simulator Center

We are opening a new golf simulator center in Copenhagen, and need a website design. We are using wordpress, and our site is https://vornlo-tee.dk
We will need a design for the frontpage, and a design for subpages (which we will be reusing for all subpages).
Logo is as seen on the site, and our base color scheme is leaf green.
As text, take the text on the current website, or put some placeholder text in english.
Should be responsive and look good on both desktop and mobile.
Target Market(s)
Male, 18-60, golf players

```html
<!DOCTYPE html>
<html lang="en">
<head>
<meta charset="utf-8">
<title>Vornlo Tee – Golf Simulator in Valby</title>
<link href="https://fonts.googleapis.com/css2?family=Oswald:wght@300;500;600;700&family=Mulish:wght@400;600;700&family=Playfair+Display:wght@900&display=swap" rel="stylesheet">
<style>
:root{
  --leaf:#0b7a1a;
  --leaf-bright:#1fa824;
  --lime:#5cc21c;
  --ink:#1a1a1a;
  --text:#333;
  --muted:#666;
  --teal:#12a98a;
  --footer:#1d1d1d;
  --white:#fff;
}
*{box-sizing:border-box;margin:0;padding:0}
html,body{width:1200px;height:3995px;overflow:hidden}
body{position:relative;font-family:"Mulish",sans-serif;color:var(--text);background:var(--white);font-size:14px;line-height:1.6}
.abs{position:absolute}
.heading{font-family:"Oswald",sans-serif;font-weight:600;color:var(--ink);text-transform:uppercase;line-height:1}
.btn{position:absolute;display:flex;align-items:center;justify-content:center;background:var(--leaf);color:var(--white);font-size:12px;font-weight:700;letter-spacing:1.5px;text-transform:uppercase;text-decoration:none}
.photo{position:absolute}

/* Header */
.site-header{position:absolute;left:0;top:0;width:1200px;height:116px;background:var(--white)}
.brand{position:absolute;display:flex;align-items:center;gap:10px;font-family:"Oswald",sans-serif;font-weight:600;font-size:38px;letter-spacing:1px;color:var(--leaf)}
.brand .mark{width:18px;height:18px;background:currentColor}
.top-contact{position:absolute;top:8px;left:648px;display:flex;align-items:center;gap:10px;font-size:13px;color:var(--ink)}
.ring{width:30px;height:30px;border:1px solid #ccc;border-radius:50%;display:flex;align-items:center;justify-content:center}
.socials{position:absolute;top:8px;left:980px;display:flex;gap:8px}
.socials span{width:30px;height:30px;border:1.5px solid #3a78c8;border-radius:50%}
.nav{position:absolute;top:62px;left:654px;display:flex;align-items:center;font-size:15px;color:var(--ink)}
.nav a{color:inherit;text-decoration:none}
.nav .active{background:var(--leaf-bright);color:var(--white);padding:8px 7px;margin-right:54px}
.nav .item{margin-right:60px}

/* Hero */
.hero{position:absolute;left:0;top:116px;width:1200px;height:616px;overflow:hidden}
.hero-photo{position:absolute;inset:0;background:
  radial-gradient(ellipse 260px 330px at 800px 250px,rgba(30,30,30,.55),rgba(30,30,30,0) 70%),
  radial-gradient(ellipse 520px 220px at 760px 80px,rgba(214,170,70,.75),rgba(214,170,70,0) 75%),
  radial-gradient(ellipse 700px 260px at 700px 560px,rgba(150,190,60,.8),rgba(150,190,60,0) 75%),
  linear-gradient(90deg,rgba(8,40,12,.85) 0%,rgba(8,40,12,.35) 30%,rgba(8,40,12,0) 55%,rgba(8,40,12,.55) 100%),
  linear-gradient(180deg,#28402a 0%,#3c6a22 55%,#5a8a2a 100%)}
.hero-line{position:absolute;background:rgba(255,255,255,.35)}
.hero-title{position:absolute;left:255px;top:190px;font-family:"Oswald",sans-serif;text-transform:uppercase;line-height:1}
.hero-title .g{display:block;color:var(--lime);font-weight:700;font-size:96px}
.hero-title .s{color:transparent;-webkit-text-stroke:2px #fff;font-weight:300;font-size:96px}
.hero-title .v{color:var(--white);font-weight:700;font-size:96px}
.hero-text{position:absolute;left:255px;top:412px;width:660px;color:var(--white);font-size:16px;line-height:1.7}
.hero .btn{left:255px;top:483px;width:122px;height:38px;background:var(--white);color:var(--ink);font-weight:600;font-size:11px}
.dots{position:absolute;top:573px;left:579px;display:flex;gap:8px}
.dots span{width:8px;height:8px;background:var(--white)}
.dots span:first-child{background:var(--lime)}

/* Intro */
.intro-kicker{position:absolute;left:612px;top:840px;font-size:22px;color:var(--ink)}
.intro-title{position:absolute;left:612px;top:878px;font-size:46px}
.intro-copy{position:absolute;left:612px;top:963px;width:512px;font-size:13.5px;line-height:1.7;color:var(--ink)}
.intro-copy p{margin-bottom:12px}

/* Simulators */
.center{text-align:center;left:0;width:1200px}
.sim-title{top:1258px;font-size:48px}
.sim-copy{top:1328px;left:195px;width:810px;text-align:center;font-size:13.5px;line-height:1.7;color:var(--ink)}

/* Reception */
.rec-kicker{left:70px;top:2003px;font-size:22px;color:var(--ink)}
.rec-title{left:70px;top:2040px;font-size:46px}
.rec-copy{left:70px;top:2118px;width:460px;font-size:13.5px;line-height:1.65;color:var(--ink)}

/* Blog */
.blog-title{top:2486px;font-size:48px}
.card-date{position:absolute;width:30px;height:46px;background:var(--lime);color:var(--white);font-size:11px;line-height:1.3;display:flex;flex-direction:column;align-items:center;justify-content:center}
.card-title{position:absolute;font-size:21px;line-height:1.2;color:var(--ink);width:338px;font-weight:400}
.card-text{position:absolute;font-size:12px;line-height:1.65;color:var(--muted);width:310px}

/* Contact */
.contact{position:absolute;left:0;top:3050px;width:1200px;height:522px;background:
  radial-gradient(ellipse 420px 260px at 640px 230px,rgba(140,190,60,.7),rgba(140,190,60,0) 75%),
  radial-gradient(ellipse 300px 200px at 1050px 420px,rgba(120,170,50,.5),rgba(120,170,50,0) 75%),
  linear-gradient(180deg,#2f7a1c 0%,#3f8a22 50%,#27621a 100%)}
.contact-art{position:absolute;left:70px;top:55px;width:390px;height:360px;background:
  radial-gradient(ellipse 60px 150px at 205px 190px,rgba(40,40,40,.55),rgba(40,40,40,0) 80%),
  radial-gradient(ellipse 180px 170px at 195px 180px,rgba(255,255,255,.18),rgba(255,255,255,0) 75%)}
.big-word{position:absolute;left:70px;top:160px;font-family:"Playfair Display",serif;font-weight:900;font-size:138px;line-height:1;color:var(--white);letter-spacing:2px}
.contact-title{left:517px;top:60px;font-size:46px;color:var(--white)}
.contact-sub{left:517px;top:118px;font-size:17px;color:var(--white)}
.field{position:absolute;background:var(--white);font-size:12px;color:#555;padding:20px 14px 0}
.contact .btn{left:517px;top:424px;width:121px;height:38px;background:var(--lime);font-size:11px}

/* Footer */
.footer{position:absolute;left:0;top:3572px;width:1200px;height:423px;background:var(--footer);color:#ddd}
.foot-h{position:absolute;top:73px;font-family:"Oswald",sans-serif;font-weight:500;color:var(--lime);font-size:20px;text-transform:uppercase}
.foot-list{position:absolute;font-size:13px;line-height:30px;color:#ddd}
.foot-contact{position:absolute;left:610px;display:flex;align-items:center;gap:10px;font-size:13px}
.foot-contact .ico{width:28px;height:28px;border:1.5px solid var(--lime);border-radius:50%;display:flex;align-items:center;justify-content:center}
.foot-socials{position:absolute;left:70px;top:193px;display:flex;gap:10px}
.foot-socials span{width:28px;height:28px;border:1px solid #555;border-radius:50%}
.news-note{position:absolute;left:882px;top:110px;width:250px;font-size:11px;line-height:1.5}
.news-input{position:absolute;left:882px;top:143px;width:247px;height:36px;background:var(--white);color:#888;font-size:11px;padding:10px 12px}
.news-btn{position:absolute;left:882px;top:190px;width:247px;height:36px;background:var(--leaf);color:var(--white);font-size:11px;display:flex;align-items:center;justify-content:center}
.foot-rule{position:absolute;left:70px;top:303px;width:1060px;height:1px;background:#333}
.foot-legal{position:absolute;left:0;top:325px;width:1200px;text-align:center;font-size:10px;line-height:1.5;color:#ddd}
.foot-legal em{font-style:normal;color:var(--lime)}
</style>
</head>
<body>

<header class="site-header">
  <div class="brand" style="left:70px;top:30px"><span>VORNLO TEE</span><span class="mark"></span></div>
  <div class="top-contact">
    <span class="ring"><svg width="14" height="14" viewBox="0 0 24 24"><path d="M6.6 10.8a15 15 0 006.6 6.6l2.2-2.2a1 1 0 011-.25 11.4 11.4 0 003.6.6 1 1 0 011 1V20a1 1 0 01-1 1A17 17 0 013 4a1 1 0 011-1h3.5a1 1 0 011 1c0 1.25.2 2.45.57 3.57a1 1 0 01-.25 1z" fill="#999"/></svg></span>
    <span style="font-weight:700;margin-right:18px">41 27 56 08</span>
    <span class="ring"><svg width="14" height="14" viewBox="0 0 24 24"><rect x="3" y="6" width="18" height="12" fill="none" stroke="#999" stroke-width="1.6"/><path d="M3 6l9 7 9-7" fill="none" stroke="#999" stroke-width="1.6"/></svg></span>
    <span>info@vornlotee.com</span>
  </div>
  <div class="socials"><span></span><span style="border-color:#3ab0e0"></span><span style="border-color:#555"></span><span style="border-color:#2a63a8"></span></div>
  <nav class="nav">
    <a class="active" href="#">Home</a>
    <a class="item" href="#">Golf simulator</a>
    <a class="item" href="#">Resources</a>
    <a href="#">About us</a>
  </nav>
</header>

<section class="hero">
  <div class="hero-photo" role="img" aria-label="Golfer putting on an indoor simulator green under a sunset screen, with a golf bag on the left"></div>
  <div class="hero-line" style="left:229px;top:164px;width:1px;height:250px"></div>
  <div class="hero-line" style="left:225px;top:295px;width:425px;height:1px"></div>
  <h1 class="hero-title"><span class="g">Golf</span><span class="s">Simulator </span><span class="v">in Valby</span></h1>
  <p class="hero-text">Indoor golf center with 8 simulators in Valby. Play golf indoors in all weathers, whether driving range or a full 18-hole round.</p>
  <a class="btn" href="#">Book now</a>
  <div class="dots"><span></span><span></span><span></span></div>
</section>

<section>
  <div class="photo" role="img" aria-label="Simulator bays with golf bags on artificial turf" style="left:72px;top:805px;width:453px;height:385px;clip-path:polygon(0 0,100% 6%,100% 94%,0 100%);background:
    radial-gradient(ellipse 60px 40px at 150px 220px,rgba(190,30,40,.6),rgba(190,30,40,0) 80%),
    radial-gradient(ellipse 50px 35px at 360px 200px,rgba(190,30,40,.55),rgba(190,30,40,0) 80%),
    radial-gradient(ellipse 30px 22px at 90px 130px,rgba(140,200,140,.6),rgba(140,200,140,0) 80%),
    radial-gradient(ellipse 30px 22px at 260px 120px,rgba(140,200,140,.5),rgba(140,200,140,0) 80%),
    linear-gradient(180deg,#2a2a2a 0%,#333 40%,#46702e 62%,#2f5a22 100%)"></div>
  <p class="intro-kicker">Golf simulator in</p>
  <h2 class="heading intro-title">Valby opens January 2023</h2>
  <div class="intro-copy">
    <p>In January 2023, a new golf simulator center will open in Valby with 8 simulators of the Swingline 4 type. We look forward to being able to welcome new and experienced golfers. With us, you can practice all kinds of shots indoors, sheltered from rain and snow, or play an entire 18-hole course in half the time.</p>
    <p>Each simulator gives you a precise radar measurement of your stroke, so you can practice exactly as you want on a virtual driving range, or on one of our many virtual courses from around the world.</p>
  </div>
</section>

<section>
  <h2 class="heading abs center sim-title">Simulators</h2>
  <p class="abs sim-copy">Vornlo Tee has 8 swingline 4 golf simulators in Valby. In the drawing above you can see how they are located in our premises in Valby. Simulator 1 is the largest and has a view of the street. Simulators 3, 4 and 5 are the same size, and are placed in a row, so that you can advantageously be in several groups together.</p>
  <div class="abs" style="left:140px;top:1397px;width:900px;height:478px;background:linear-gradient(180deg,#e4e4e4,#f0f0f0);clip-path:polygon(0 0,100% 4%,100% 100%,0 100%)"></div>
  <div class="photo" role="img" aria-label="Golfer putting in front of a simulator screen showing a fairway, set against a teal panel" style="left:162px;top:1427px;width:878px;height:418px;background:
    radial-gradient(ellipse 90px 200px at 500px 230px,rgba(60,50,40,.55),rgba(60,50,40,0) 80%),
    radial-gradient(ellipse 200px 70px at 210px 90px,rgba(200,220,235,.7),rgba(200,220,235,0) 80%),
    linear-gradient(90deg,transparent 0 48.5%,var(--teal) 48.5% 100%),
    linear-gradient(180deg,#b9d3e0 0%,#6d9a48 28%,#5b8a36 60%,#3f6a28 100%)"></div>
</section>

<section>
  <div class="abs" style="left:820px;top:1920px;width:380px;height:497px;background:var(--leaf)"></div>
  <p class="abs rec-kicker">Opening</p>
  <h2 class="heading abs rec-title">Reception</h2>
  <p class="abs rec-copy">We will hold an opening reception on 20 January 2023 from 4 p.m. More information will be available on this page continuously, and via our newsletter, which you can sign up for here. We also give a discount code for 1 hour of free play to everyone who signs up for our newsletter before the New Year and who is still signed up for the newsletter at our opening reception.</p>
  <a class="btn" href="#" style="left:70px;top:2287px;width:123px;height:39px">Read more</a>
  <div class="photo" role="img" aria-label="Tablet showing two golfers at a simulator" style="left:590px;top:2010px;width:465px;height:315px;border-radius:22px;box-shadow:0 18px 30px rgba(0,0,0,.35);background:
    radial-gradient(ellipse 170px 110px at 230px 150px,rgba(120,170,70,.9),rgba(120,170,70,0) 80%),
    radial-gradient(ellipse 200px 80px at 230px 80px,rgba(90,130,210,.8),rgba(90,130,210,0) 80%),
    linear-gradient(135deg,#222,#2b2b2b 20%,#3a4a5a 50%,#2e4a24 80%,#1a1a1a);transform:rotate(4deg)"></div>
</section>

<section>
  <h2 class="heading abs center blog-title">Recent blog</h2>

  <div class="photo" role="img" aria-label="Golfer swinging in a simulator bay" style="left:70px;top:2566px;width:338px;height:214px;background:
    radial-gradient(ellipse 90px 60px at 220px 75px,rgba(120,190,110,.8),rgba(120,190,110,0) 80%),
    radial-gradient(ellipse 40px 90px at 95px 110px,rgba(200,200,200,.35),rgba(200,200,200,0) 80%),
    linear-gradient(180deg,#2a2e2a 0%,#2f3a2f 55%,#3e6a2c 75%,#2c4d22 100%)"></div>
  <div class="card-date" style="left:78px;top:2750px"><span>22</span><span>Dec</span></div>
  <h3 class="card-title" style="left:70px;top:2815px">The first blow has been struck!</h3>
  <p class="card-text" style="left:70px;top:2855px">The first blow on the first simulator has been struck, and now we just need to have the other 7 completed.</p>
  <a class="btn" href="#" style="left:70px;top:2940px;width:122px;height:38px">Read more</a>

  <div class="photo" role="img" aria-label="Golfers at a simulator showing a city sunset and a target green" style="left:431px;top:2566px;width:338px;height:214px;background:
    radial-gradient(ellipse 70px 22px at 170px 125px,rgba(230,80,70,.8),rgba(230,80,70,0) 80%),
    radial-gradient(ellipse 160px 60px at 170px 90px,rgba(240,170,70,.85),rgba(240,170,70,0) 80%),
    linear-gradient(180deg,#2a3558 0%,#4a4a6a 30%,#a87a3e 50%,#4a7a2e 72%,#243a1a 100%)"></div>
  <div class="card-date" style="left:444px;top:2750px"><span>04</span><span>Aug</span></div>
  <h3 class="card-title" style="left:431px;top:2815px">Golf training on a simulator</h3>
  <p class="card-text" style="left:431px;top:2855px">Golf training can be done directly on a golf simulator at Vornlo Tee in Valby. Here you get the opportunity to train with a Pro, or train yourself.</p>
  <a class="btn" href="#" style="left:431px;top:2940px;width:122px;height:38px">Read more</a>

  <div class="photo" role="img" aria-label="Golf clubs in a bag in front of a painted wall" style="left:791px;top:2566px;width:338px;height:214px;background:
    radial-gradient(ellipse 90px 50px at 90px 100px,rgba(200,80,80,.5),rgba(200,80,80,0) 80%),
    radial-gradient(ellipse 80px 100px at 300px 90px,rgba(230,230,220,.45),rgba(230,230,220,0) 80%),
    radial-gradient(ellipse 100px 70px at 200px 160px,rgba(160,160,165,.6),rgba(160,160,165,0) 80%),
    linear-gradient(180deg,#d8cdb8 0%,#b7a58a 30%,#6e5a4a 65%,#2f2a26 100%)"></div>
  <div class="card-date" style="left:805px;top:2750px"><span>02</span><span>July</span></div>
  <h3 class="card-title" style="left:791px;top:2813px">Golf equipment for use on a simulator</h3>
  <p class="card-text" style="left:791px;top:2875px">Play golf in Valby at Vornlo Tee. With us you can play indoors in dry weather...</p>
  <a class="btn" href="#" style="left:791px;top:2940px;width:122px;height:38px">Read more</a>
</section>

<section class="contact">
  <div class="big-word">GOLF</div>
  <div class="contact-art" role="img" aria-label="Golfer in follow-through in front of the lettering"></div>
  <h2 class="heading abs contact-title">Contact us</h2>
  <p class="abs contact-sub">Write to us via the form below, or directly at info@vornlo-tee.dk</p>
  <div class="field" style="left:517px;top:167px;width:298px;height:51px">Name:</div>
  <div class="field" style="left:826px;top:167px;width:298px;height:51px">Email:</div>
  <div class="field" style="left:517px;top:228px;width:607px;height:52px">Subjects:</div>
  <div class="field" style="left:517px;top:290px;width:613px;height:122px">Message:</div>
  <a class="btn" href="#">Submit</a>
</section>

<footer class="footer">
  <div class="brand" style="left:70px;top:95px;color:var(--white)"><span>VORNLO TEE</span><span class="mark"></span></div>
  <div class="foot-socials"><span></span><span></span><span></span><span></span></div>

  <h4 class="foot-h" style="left:408px">Quick links</h4>
  <div class="foot-list" style="left:409px;top:110px">Golf simulator<br>Resources<br>About us</div>

  <h4 class="foot-h" style="left:610px">Contact</h4>
  <div class="foot-contact" style="top:113px"><span class="ico"><svg width="12" height="12" viewBox="0 0 24 24"><path d="M12 2a7 7 0 00-7 7c0 5 7 13 7 13s7-8 7-13a7 7 0 00-7-7zm0 9.5A2.5 2.5 0 1112 6.5a2.5 2.5 0 010 5z" fill="#5cc21c"/></svg></span>Stenholtvej 14 2500 Valby</div>
  <div class="foot-contact" style="top:160px"><span class="ico"><svg width="12" height="12" viewBox="0 0 24 24"><path d="M6.6 10.8a15 15 0 006.6 6.6l2.2-2.2a1 1 0 011-.25 11.4 11.4 0 003.6.6 1 1 0 011 1V20a1 1 0 01-1 1A17 17 0 013 4a1 1 0 011-1h3.5a1 1 0 011 1c0 1.25.2 2.45.57 3.57a1 1 0 01-.25 1z" fill="#5cc21c"/></svg></span>41 27 56 08</div>
  <div class="foot-contact" style="top:207px"><span class="ico"><svg width="12" height="12" viewBox="0 0 24 24"><rect x="3" y="6" width="18" height="12" fill="#5cc21c"/><path d="M3 6l9 7 9-7" fill="none" stroke="#1d1d1d" stroke-width="1.6"/></svg></span>info@vornlotee.com</div>

  <h4 class="foot-h" style="left:880px">Book golf simulator</h4>
  <p class="news-note">Unfortunately, we are not open for bookings yet. We have an opening reception on 20 January.</p>
  <div class="news-input">Enter Your Email</div>
  <div class="news-btn">Yes Please!</div>

  <div class="foot-rule"></div>
  <p class="foot-legal">Personal data policy &nbsp;|&nbsp; Conditions for membership<br>COPYRIGHT © 2023 <em>VORNLO TEE</em>. ALL RIGHTS RESERVED.</p>
</footer>

</body>
</html>
```